I need a creative wine label design for my brand called ZAP ZEE. A design that catches the eye of the millennial consumer! Something very creative and playing off of the ZAP ZEE concept.

This will be a Red Blend 2019 vintage from California

Target Market(s)

Millennial wine consumer

Requirements
Must have
• Must have a design that attracts the millennial wine consumer. This must have creative flare.
Should not have
• Nothing corny!

```html
<!DOCTYPE html>
<html lang="en">
<head>
<meta charset="utf-8">
<title>ZAP ZEE California Red Blend 2019 – Wine Label</title>
<link rel="stylesheet" href="https://fonts.googleapis.com/css2?family=Jost:wght@300;400&display=swap">
<style>
  :root {
    --wine-red: #560808;
    --wine-red-deep: #3f0505;
    --wine-red-glow: #6a0c0c;
    --gold: #c9a24a;
    --gold-light: #e0c06a;
    --cream: #f1e4a2;
    --white: #ffffff;
  }
  html, body {
    margin: 0;
    padding: 0;
    width: 990px;
    height: 1200px;
    overflow: hidden;
    background: var(--wine-red);
  }
  .label {
    position: relative;
    width: 990px;
    height: 1200px;
    overflow: hidden;
    font-family: "Jost", sans-serif;
  }
  .label__pattern {
    position: absolute;
    inset: 0;
    background:
      radial-gradient(ellipse 420px 300px at 50% 53%, var(--wine-red-glow) 0%, rgba(106, 12, 12, 0) 100%),
      radial-gradient(ellipse 260px 200px at 12% 30%, rgba(63, 5, 5, 0.7) 0%, rgba(63, 5, 5, 0) 100%),
      radial-gradient(ellipse 260px 200px at 88% 30%, rgba(63, 5, 5, 0.7) 0%, rgba(63, 5, 5, 0) 100%),
      radial-gradient(ellipse 300px 240px at 15% 80%, rgba(63, 5, 5, 0.7) 0%, rgba(63, 5, 5, 0) 100%),
      radial-gradient(ellipse 300px 240px at 85% 80%, rgba(63, 5, 5, 0.7) 0%, rgba(63, 5, 5, 0) 100%),
      linear-gradient(180deg, var(--wine-red-deep) 0%, var(--wine-red) 30%, var(--wine-red) 70%, var(--wine-red-deep) 100%);
  }
  .brand {
    position: absolute;
    top: 110px;
    left: 90px;
    width: 815px;
    height: 200px;
    margin: 0;
    display: flex;
    align-items: center;
    justify-content: space-between;
    font-weight: 400;
    font-size: 185px;
    line-height: 200px;
    color: var(--gold);
  }
  .brand__word {
    letter-spacing: 10px;
    margin-right: -10px;
  }
  .brand__mark {
    flex: none;
    width: 110px;
    height: 110px;
    border-radius: 50%;
    background: var(--gold);
    margin-top: 14px;
  }
  .brand-rule {
    position: absolute;
    top: 325px;
    left: 165px;
    width: 660px;
    height: 3px;
    background: var(--cream);
  }
  .region {
    position: absolute;
    top: 350px;
    left: 165px;
    width: 662px;
    margin: 0;
    display: flex;
    justify-content: space-between;
    font-weight: 300;
    font-size: 54px;
    line-height: 64px;
    color: var(--cream);
  }
  .varietal {
    position: absolute;
    top: 880px;
    left: 0;
    width: 100%;
    margin: 0;
    text-align: center;
    font-weight: 400;
    font-size: 92px;
    line-height: 100px;
    letter-spacing: 4px;
    text-indent: 4px;
    color: var(--white);
  }
  .vintage {
    position: absolute;
    top: 1090px;
    left: 0;
    width: 100%;
    margin: 0;
    text-align: center;
    font-weight: 300;
    font-size: 66px;
    line-height: 74px;
    letter-spacing: 20px;
    text-indent: 20px;
    color: var(--cream);
  }
</style>
</head>
<body>
  <main class="label">
    <div class="label__pattern" role="img" aria-label="Tonal dark red ornamental tile pattern covering the whole label"></div>

    <h1 class="brand" aria-label="ZAP ZEE">
      <span class="brand__word">ZAP</span>
      <span class="brand__mark"></span>
      <span class="brand__word">ZEE</span>
    </h1>
    <div class="brand-rule"></div>
    <p class="region" aria-label="California">
      <span>C</span><span>A</span><span>L</span><span>I</span><span>F</span><span>O</span><span>R</span><span>N</span><span>I</span><span>A</span>
    </p>

    <h2 class="varietal">RED BLEND</h2>
    <p class="vintage">2019</p>
  </main>
</body>
</html>
```